Digital Album Cover - Vellorin Tamsuvel Under Copper Skies (Piano & Cello)

Hi
I would like a digital album cover

Title: "Under Copper Skies (Piano & Cello)"
Artist: "Caleb Rourke & The Pell Orsola"

Preview of instrumental song:
https://tunevault-example.net/calebrourkepianist/tamsuvel-under-copper-skies-piano-and-cello

```html
<!DOCTYPE html>
<html lang="en">
<head>
<meta charset="utf-8">
<title>Under Copper Skies (Piano &amp; Cello) — Caleb Rourke &amp; The Pell Orsola</title>
<link rel="stylesheet" href="https://fonts.googleapis.com/css2?family=Nunito+Sans:wght@600&family=Playfair+Display:wght@400&display=swap">
<style>
  :root {
    --page-bg: #e2e2e2;
    --sky-gold: #f6c24a;
    --sky-amber: #d98a1c;
    --sky-copper: #9a5418;
    --shade-brown: #3d2414;
    --sun-glow: #fff3b8;
    --water-dark: #5a3417;
    --ink-light: #ffffff;
  }
  * { margin: 0; padding: 0; box-sizing: border-box; }
  html, body {
    width: 1200px;
    height: 1040px;
    overflow: hidden;
    background: var(--page-bg);
  }
  .album-cover {
    position: absolute;
    left: 120px;
    top: 40px;
    width: 960px;
    height: 960px;
    overflow: hidden;
    box-shadow: 0 6px 14px rgba(0, 0, 0, 0.25);
  }
  .cover-artwork {
    position: absolute;
    inset: 0;
    background:
      radial-gradient(circle at 4% 49%, var(--sun-glow) 0%, rgba(255, 230, 140, 0.85) 8%, rgba(246, 194, 74, 0) 32%),
      radial-gradient(ellipse 38% 55% at 88% 62%, rgba(40, 24, 14, 0.85) 0%, rgba(60, 34, 18, 0.55) 55%, rgba(60, 34, 18, 0) 100%),
      linear-gradient(180deg, rgba(61, 36, 20, 0.55) 0%, rgba(61, 36, 20, 0) 22%, rgba(0, 0, 0, 0) 70%, rgba(90, 52, 23, 0.7) 100%),
      linear-gradient(100deg, var(--sky-gold) 0%, var(--sky-amber) 45%, var(--sky-copper) 80%, var(--shade-brown) 100%);
  }
  .cover-title {
    position: absolute;
    left: 538px;
    top: 200px;
    transform: translateX(-50%);
    font-family: "Nunito Sans", sans-serif;
    font-weight: 600;
    font-size: 100px;
    line-height: 127px;
    letter-spacing: 1px;
    text-align: center;
    text-transform: uppercase;
    color: var(--ink-light);
    white-space: nowrap;
  }
  .cover-title span { display: block; }
  .cover-artist {
    position: absolute;
    left: 0;
    right: 0;
    top: 904px;
    transform: translateX(-2%);
    font-family: "Playfair Display", serif;
    font-size: 29px;
    letter-spacing: 0.5px;
    text-align: center;
    text-transform: uppercase;
    color: var(--ink-light);
    white-space: nowrap;
  }
  .cover-artist .amp { font-size: 19px; }
</style>
</head>
<body>
  <main class="album-cover">
    <div class="cover-artwork" role="img" aria-label="Fantasy illustration: a couple in evening wear dancing on glassy water beneath a glowing copper sunset sky, with a crooked storybook house lit by blue windows rising from the water on the right"></div>
    <h1 class="cover-title">
      <span>Under</span>
      <span>Copper</span>
      <span>Skies</span>
    </h1>
    <p class="cover-artist">Caleb Rourke <span class="amp">&amp;</span> The Pell Orsola</p>
  </main>
</body>
</html>
```